Criminal Defense Firm looking for an edge in business card design

Established Criminal Defense Firm looking to refresh business card. We already have logo and website, but our business cards are extremely boring. We would like to also have something on the backside of card.
Needs to be business oriented, but creative.
We provide services to professionals such as doctors, lawyers, politicians, etc.
Our specialty is to protect professional licenses when facing a criminal matter.

Update on March 10, 2015: This project is for a Business Card Design. The winner in this project will be assigned the next (1on1) project which incidentally is also entitled Business Card Design. I'm sorry for this confusion. The 1on1 project will not be for Business Card Design but will be for Stationery-Envelope Design. Thank you for your attention and continued participation.

Target Market(s)

People accused of a crime

Industry/Entity Type

Business

Contact Information for Business Card

Simple, strong, professional

Colors
85abd2
3176b5
0355a3

```html
<!DOCTYPE html>
<html lang="en">
<head>
<meta charset="utf-8">
<title>Whitcombe Garland – Business Card</title>
<link rel="stylesheet" href="https://fonts.googleapis.com/css2?family=Crimson+Text:ital,wght@0,400;0,700;1,400&family=Yanone+Kaffeesatz:wght@300;400&display=swap">
<style>
  :root {
    --brand-blue: #2f7bbd;
    --brand-deep: #0355a3;
    --brand-light: #85abd2;
    --card-white: #ffffff;
    --ink-grey: #666b70;
    --page-bg: #e9eaec;
  }
  * { box-sizing: border-box; margin: 0; padding: 0; }
  html, body { width: 1200px; height: 1000px; overflow: hidden; }
  body {
    background: var(--page-bg);
    display: flex;
    align-items: center;
    justify-content: center;
    gap: 60px;
  }
  .card {
    width: 340px;
    height: 595px;
    position: relative;
    box-shadow: 0 6px 18px rgba(0,0,0,0.18);
    overflow: hidden;
  }
  /* Front */
  .card-front { background: var(--card-white); display: flex; flex-direction: column; }
  .name-band {
    background: var(--brand-blue);
    padding: 18px 22px 14px;
    color: var(--card-white);
    text-align: right;
  }
  .person-name {
    font-family: "Crimson Text", serif;
    font-weight: 700;
    font-size: 31px;
    line-height: 1;
  }
  .person-title {
    font-family: "Yanone Kaffeesatz", sans-serif;
    font-weight: 300;
    font-size: 19px;
    letter-spacing: 2px;
    margin-top: 4px;
  }
  .contact-list {
    list-style: none;
    padding: 30px 26px 0 30px;
    flex: 1;
  }
  .contact-item {
    display: flex;
    align-items: flex-start;
    gap: 14px;
    margin-bottom: 30px;
    font-family: "Yanone Kaffeesatz", sans-serif;
    font-weight: 300;
    font-size: 22px;
    line-height: 1.1;
    color: var(--ink-grey);
  }
  .contact-icon { width: 22px; height: 22px; flex: none; fill: var(--brand-blue); margin-top: 1px; }
  .firm-mark {
    display: flex;
    align-items: center;
    gap: 12px;
    padding: 0 26px 18px 30px;
  }
  .firm-dot {
    width: 44px; height: 44px; border-radius: 50%;
    background: var(--brand-blue);
    flex: none;
  }
  .firm-name {
    font-family: "Crimson Text", serif;
    font-weight: 700;
    font-size: 21px;
    line-height: 1;
    color: var(--brand-blue);
  }
  .firm-suffix {
    font-family: "Crimson Text", serif;
    font-size: 13px;
    color: var(--ink-grey);
    margin-top: 3px;
  }
  .tagline-band {
    background: var(--brand-blue);
    color: var(--card-white);
    font-family: "Crimson Text", serif;
    font-style: italic;
    font-size: 19px;
    line-height: 1.15;
    text-align: center;
    padding: 14px 18px 16px;
  }
  /* Back */
  .card-back {
    background: var(--brand-blue);
    display: flex;
    align-items: center;
    justify-content: center;
  }
  .back-seal {
    width: 200px; height: 200px;
    border-radius: 50%;
    border: 8px solid var(--card-white);
    display: flex;
    align-items: center;
    justify-content: center;
    text-align: center;
    font-family: "Crimson Text", serif;
    font-weight: 700;
    font-size: 30px;
    line-height: 1.05;
    color: var(--card-white);
  }
</style>
</head>
<body>
  <article class="card card-front">
    <header class="name-band">
      <h1 class="person-name">Daniel Whitcombe</h1>
      <p class="person-title">ATTORNEY AT LAW</p>
    </header>
    <ul class="contact-list">
      <li class="contact-item">
        <svg class="contact-icon" viewBox="0 0 24 24" aria-hidden="true"><path d="M2 6h20v12H2z" opacity=".9"/><path d="M2 6l10 7 10-7" fill="none" stroke="#fff" stroke-width="1.6"/></svg>
        <span>dan@wgdefenselaw.com</span>
      </li>
      <li class="contact-item">
        <svg class="contact-icon" viewBox="0 0 24 24" aria-hidden="true"><path d="M12 2a7 7 0 0 0-7 7c0 5 7 13 7 13s7-8 7-13a7 7 0 0 0-7-7zm0 9.5A2.5 2.5 0 1 1 12 6.5a2.5 2.5 0 0 1 0 5z"/></svg>
        <span>1820 Alder Avenue, Suite 210<br>Riverton, California 93650</span>
      </li>
      <li class="contact-item">
        <svg class="contact-icon" viewBox="0 0 24 24" aria-hidden="true"><path d="M6.6 10.8a15 15 0 0 0 6.6 6.6l2.2-2.2a1 1 0 0 1 1-.25 11.4 11.4 0 0 0 3.6.6 1 1 0 0 1 1 1V20a1 1 0 0 1-1 1A17 17 0 0 1 3 4a1 1 0 0 1 1-1h3.5a1 1 0 0 1 1 1c0 1.250.2 2.45.6 3.6a1 1 0 0 1-.25 1z"/></svg>
        <span>555.310.4821</span>
      </li>
      <li class="contact-item">
        <svg class="contact-icon" viewBox="0 0 24 24" aria-hidden="true"><path d="M7 3h10v5H7z"/><path d="M4 9h16a2 2 0 0 1 2 2v6h-4v-3H6v3H2v-6a2 2 0 0 1 2-2z"/><path d="M7 15h10v6H7z"/></svg>
        <span>555.310.4822</span>
      </li>
    </ul>
    <div class="firm-mark">
      <span class="firm-dot" aria-hidden="true"></span>
      <div>
        <p class="firm-name">Whitcombe Garland</p>
        <p class="firm-suffix">Law Corporation</p>
      </div>
    </div>
    <footer class="tagline-band">Seasoned criminal defense counsel<br>on your side when it counts</footer>
  </article>

  <article class="card card-back">
    <div class="back-seal">Whitcombe<br>Garland</div>
  </article>
</body>
</html>
```